Fun modern label needed for olive oil bottle

I need a label for a boutique handmade olive oil line. It needs to be fun and reflect the smallness of the operation and from rural Australia

The name of the line comes from the fact that I live in rural Australia and the black tar road ends 5 km from my home. The road turns to dusty slippery gravel in summer and wet and slippery gravel mud in winter.
Those of us who live out here say that the best people live WATTLE CREEK HOLLOW.

There are no restrictions on colours but it MUST be fun with clear strong lines.

The label is rectangular with the short sides top and bottom. I shall measure the bottles later today and update the brief for you

Below is an example of the bottles used and there will be 3 different sizes
Updates

I have added a couple of photos to show Australian labels and what is need on them sorry to have left out this crucial information

Industry/Entity Type

Boutique

Requirements
Must have
• Wattle Creek Hollow as name
Some sort of logo

```html
<!DOCTYPE html>
<html lang="en">
<head>
<meta charset="utf-8">
<title>Wattle Creek Hollow – Hand Made Olive Oil Label</title>
<link rel="stylesheet" href="https://fonts.googleapis.com/css2?family=Tinos:wght@400;700&display=swap">
<style>
  :root {
    --night: #050505;
    --earth: #52200f;
    --olive: #566b31;
    --wattle: #f5d000;
    --clay: #7a2d17;
    --clay-deep: #4a1a0c;
    --ink: #0a0a0a;
  }
  * { box-sizing: border-box; margin: 0; padding: 0; }
  html, body { width: 849px; height: 1200px; overflow: hidden; background: var(--night); }
  body { font-family: "Tinos", "Times New Roman", serif; color: var(--wattle); }
  .canvas { position: relative; width: 849px; height: 1200px; background: var(--night); }

  .label { position: absolute; top: 133px; width: 346px; height: 935px; }
  .label--front { left: 59px; }
  .label--back { left: 446px; }
  .label__art { position: absolute; inset: 0; width: 100%; height: 100%; display: block; }

  .front__title {
    position: absolute; top: 26px; left: 0; width: 100%;
    text-align: center; font-weight: 700; font-size: 20px; line-height: 33px; letter-spacing: 0.5px;
  }
  .front__footer {
    position: absolute; top: 870px; left: 0; width: 100%;
    text-align: center; font-size: 14px; line-height: 21px; font-weight: 400;
  }
  .brand-arc { font-family: "Tinos", "Times New Roman", serif; font-weight: 700; font-size: 40px; fill: var(--wattle); }

  .back__ingredients { position: absolute; top: 140px; left: 15px; width: 325px; }
  .ingredients__heading { font-size: 18px; font-weight: 400; line-height: 28px; }
  .ingredients__item { font-size: 17.5px; font-weight: 700; line-height: 28px; white-space: nowrap; }
  .ingredients__storage { font-size: 16.5px; font-weight: 400; line-height: 25px; margin-top: 3px; }

  .nutrition {
    position: absolute; top: 355px; left: 16px; width: 313px; height: 314px;
    border: 3px solid var(--wattle); border-radius: 16px; padding: 13px 9px 0 9px;
    font-weight: 700;
  }
  .nutrition__title { font-size: 14.5px; font-weight: 700; line-height: 18px; letter-spacing: 0.2px; }
  .nutrition__servings { font-size: 10.5px; margin-top: 14px; line-height: 13px; white-space: nowrap; }
  .nutrition__table { width: 100%; border-collapse: collapse; margin-top: 17px; font-size: 10.5px; }
  .nutrition__table td { height: 17.1px; padding: 0; line-height: 13px; white-space: nowrap; }
  .nutrition__table .qty { text-align: right; }
  .nutrition__table .col-serve { width: 78px; }
  .nutrition__table .col-hundred { width: 86px; }

  .barcode-slot {
    position: absolute; top: 700px; left: 17px; width: 181px; height: 76px;
    border: 2px solid var(--ink); display: flex; align-items: center; justify-content: center;
    color: var(--ink); font-weight: 700; font-size: 16px;
  }
</style>
</head>
<body>
<main class="canvas">

  <section class="label label--front">
    <svg class="label__art" viewBox="0 0 407 1101" preserveAspectRatio="none">
      <defs>
        <clipPath id="front-shape"><rect x="0" y="0" width="407" height="1101" rx="38"/></clipPath>
        <radialGradient id="scene-tone" cx="0.5" cy="0.5" r="0.6">
          <stop offset="0" stop-color="var(--clay)"/>
          <stop offset="1" stop-color="var(--clay-deep)"/>
        </radialGradient>
        <path id="brand-path" d="M 11 420 A 235 235 0 0 1 395 420"/>
      </defs>
      <g clip-path="url(#front-shape)">
        <rect class="field" width="407" height="1101" fill="var(--olive)"/>
        <path class="band-top" d="M0 0 H407 V145 Q203.5 112 0 145 Z" fill="var(--earth)"/>
        <path class="band-bottom" d="M0 953 Q203.5 993 407 953 V1101 H0 Z" fill="var(--earth)"/>
      </g>
      <g role="img" aria-label="Olive branch wreath ornament above the brand name">
        <path d="M 2 360 A 290 290 0 0 1 404 360" fill="none" stroke="var(--wattle)" stroke-opacity="0.3" stroke-width="60"/>
      </g>
      <g role="img" aria-label="Olive branch wreath ornament below the landscape">
        <path d="M 12 700 A 240 240 0 0 0 394 700" fill="none" stroke="var(--wattle)" stroke-opacity="0.3" stroke-width="60"/>
      </g>
      <text class="brand-arc" text-anchor="middle"><textPath href="#brand-path" startOffset="50%">Wattle Creek Hollow</textPath></text>
      <circle role="img" aria-label="Photograph of an outback dirt road" cx="203" cy="555" r="197" fill="url(#scene-tone)" stroke="var(--wattle)" stroke-width="3"/>
      <rect class="frame" x="2.5" y="2.5" width="402" height="1096" rx="36" fill="none" stroke="var(--wattle)" stroke-width="5"/>
    </svg>
    <h1 class="front__title">HAND MADE<br>OLIVE OIL</h1>
    <p class="front__footer">750ml<br>PRODUCT OF AUSTRALIA</p>
  </section>

  <section class="label label--back">
    <svg class="label__art" viewBox="0 0 407 1101" preserveAspectRatio="none" aria-hidden="true">
      <defs>
        <clipPath id="back-shape"><rect x="0" y="0" width="407" height="1101" rx="38"/></clipPath>
      </defs>
      <g clip-path="url(#back-shape)">
        <rect width="407" height="1101" fill="var(--olive)"/>
        <path d="M0 0 H407 V145 Q203.5 112 0 145 Z" fill="var(--earth)"/>
        <path d="M0 953 Q203.5 993 407 953 V1101 H0 Z" fill="var(--earth)"/>
      </g>
      <rect x="2.5" y="2.5" width="402" height="1096" rx="36" fill="none" stroke="var(--wattle)" stroke-width="5"/>
    </svg>

    <div class="back__ingredients">
      <h2 class="ingredients__heading">INGREDIENTS:</h2>
      <p class="ingredients__item">100% Australian Extra Virgin Olive Oil.</p>
      <p class="ingredients__storage">Store in a cool dark place away from<br>light and heat.</p>
    </div>

    <div class="nutrition">
      <h2 class="nutrition__title">NUTRITION INFORMATION</h2>
      <p class="nutrition__servings">SERVINGS PER PACKAGE: 50 SERVING SIZE: 15ml</p>
      <table class="nutrition__table">
        <tr><td>AVERAGE QUANTITY</td><td class="qty col-serve">PER 15ml</td><td class="qty col-hundred">PER 100ml</td></tr>
        <tr><td>ENERGY - Kj</td><td class="qty">517kj</td><td class="qty">3447kj</td></tr>
        <tr><td>PROTEIN</td><td class="qty">0.0g</td><td class="qty">0.0g</td></tr>
        <tr><td>FAT</td><td class="qty"></td><td class="qty"></td></tr>
        <tr><td>-TOTAL</td><td class="qty">13.7g</td><td class="qty">91.5g</td></tr>
        <tr><td>-SATURATED</td><td class="qty">2.0g</td><td class="qty">13.5g</td></tr>
        <tr><td>-MONOUNSATURATED</td><td class="qty">10.3g</td><td class="qty">68.7g</td></tr>
        <tr><td>-POLYUNSATURATED</td><td class="qty">1.4g</td><td class="qty">9.3g</td></tr>
        <tr><td>-TRANS</td><td class="qty">&lt;0.01g</td><td class="qty">&lt;0.05g</td></tr>
        <tr><td>SHOLESTEROL</td><td class="qty">0.0mg</td><td class="qty">0.0mg</td></tr>
        <tr><td>CARBOHYDRATE</td><td class="qty">0.0g</td><td class="qty">0.0g</td></tr>
        <tr><td>-SUGARS</td><td class="qty">0.0g</td><td class="qty">0.0g</td></tr>
        <tr><td>SODIUM</td><td class="qty">0.0mg</td><td class="qty">0.0mg</td></tr>
      </table>
    </div>

    <div class="barcode-slot">place for barcode</div>
  </section>

</main>
</body>
</html>
```